Research and Development Technical Training for Process Engineering

We are creating a Portal site that will contain links to several training materials. I will create and upload the content, just looking for graphics and a basic layout for a single homepage. The page should contain unique graphics for the following topics/categories: Methodology, Equipment Training, Design References, Safety & Environmental, and Technology. (See attached example. Layout example DOES NOT need to be followed, only an example).
Also, a graphic to be used for a Powerpoint template that is cohesive with the graphics previously mentioned. Space for a company logo required. Professional/business application. Company logo already exists, it is blue and red but these colors are not required to be used as a theme.
Industry/Entity Type
Training
Number of Pages Required
1 page
Colors
Designer to choose colors to be used in the design.
Look and feel

```html
<!DOCTYPE html>
<html lang="en">
<head>
<meta charset="utf-8">
<title>Research and Development Training</title>
<link rel="stylesheet" href="https://fonts.googleapis.com/css2?family=Montserrat:wght@500;600;700;800&family=Open+Sans:wght@400;600;700&display=swap">
<style>
:root{
  --sky:#5cc0ea;
  --sky-light:#8fd6f3;
  --sun:#ffcf2e;
  --navy:#123f80;
  --navy-deep:#0b3270;
  --footer:#0a2a5e;
  --red:#e8174a;
  --ink:#1d2a44;
  --body:#4a4f58;
  --muted:#6a6e75;
  --line:#c9ced6;
  --pale:#f2f7fb;
  --star:#f2a416;
  --price:#2a76c9;
  --white:#ffffff;
}
*{box-sizing:border-box;margin:0;padding:0}
html,body{width:1200px;height:3163px;overflow:hidden}
body{position:relative;background:var(--white);font-family:"Open Sans",Arial,sans-serif;color:var(--body)}
.abs{position:absolute}
h2,h3{font-weight:inherit}

/* header */
.hero{left:0;top:0;width:1200px;height:432px;background:var(--sky)}
.hero-art{left:0;top:0;width:1200px;height:432px;
  background:
    radial-gradient(ellipse 20% 30% at 50% 34%,rgba(255,207,46,.85) 0,rgba(255,207,46,.35) 55%,rgba(255,207,46,0) 100%),
    radial-gradient(ellipse 42% 70% at 50% 50%,rgba(190,232,250,.7) 0,rgba(143,214,243,.35) 55%,rgba(92,192,234,0) 100%),
    linear-gradient(180deg,#6cc8ee 0,var(--sky) 100%)}
.brand{left:84px;top:22px;display:flex;align-items:center;gap:10px;font-family:"Montserrat",Arial,sans-serif;font-weight:800;font-size:27px;color:var(--white);letter-spacing:1px}
.brand-mark{width:22px;height:22px;background:var(--red)}
.top-links{right:84px;top:12px;display:flex;gap:42px;align-items:center;font-family:"Montserrat",Arial,sans-serif;font-weight:600;font-size:14px;color:var(--white);letter-spacing:1px}
.top-links span{display:flex;align-items:center;gap:12px}

/* title band */
.title-band{left:0;top:432px;width:1200px;height:91px;background:var(--pale);border-bottom:3px solid #e3e8ee;display:flex;align-items:center;justify-content:center;font-family:"Montserrat",Arial,sans-serif;font-weight:700;font-size:32px;letter-spacing:5px;color:var(--navy)}
.title-band em{font-style:normal;color:var(--red);margin-left:14px}

/* headings */
.section-title{font-family:"Montserrat",Arial,sans-serif;font-weight:700;font-size:30px;letter-spacing:2px;color:var(--ink);padding-bottom:6px;border-bottom:3px solid var(--red)}
.section-title em{font-style:normal;color:var(--red)}
.centered{left:0;width:1200px;display:flex;justify-content:center}

/* about */
.about-title{left:84px;top:575px}
.about-title .section-title{border-bottom:0;background:linear-gradient(90deg,var(--navy),var(--red),#f5b52b) bottom/100% 3px no-repeat}
.about-text{left:84px;top:648px;width:624px;font-size:14px;line-height:24.5px;color:var(--body)}
.about-art{left:760px;top:586px;width:440px;height:352px;
  background:
    radial-gradient(ellipse 38% 34% at 68% 30%,rgba(63,163,214,.45),rgba(63,163,214,0) 100%),
    linear-gradient(180deg,#eef2f6 0,#dfe5eb 100%)}

/* categories */
.categories{left:0;top:1002px;width:1200px;height:970px;background:linear-gradient(180deg,#f7f8fa 0,#eef0f3 48%,#8a8d92 54%,#2a2a2a 62%,#161616 100%)}
.cat-card{background:var(--white);border:1px solid var(--line);border-radius:3px;overflow:hidden}
.cat-img{width:100%}
.cat-bar{display:flex;align-items:center;justify-content:center;background:var(--navy);color:var(--white);font-family:"Montserrat",Arial,sans-serif;font-weight:500;font-size:21px;letter-spacing:1px}
.cat-bar.active{background:var(--red)}
.cat-text{font-size:14px;line-height:22px;text-align:center;padding:14px 22px;color:var(--muted)}
.row-one .cat-card{top:1132px;width:327px;height:376px}
.row-one .cat-img{height:200px}
.row-one .cat-bar{height:53px}
.row-two .cat-card{top:1535px;width:500px;height:369px}
.row-two .cat-img{height:169px}
.row-two .cat-bar{height:51px}
.row-two .cat-text{padding:26px 30px}

/* courses */
.course{top:2103px;width:238px;height:365px;background:var(--white);box-shadow:0 2px 6px rgba(0,0,0,.18)}
.course-img{height:175px}
.course-body{padding:10px 16px 0}
.course-title{font-family:"Open Sans",Arial,sans-serif;font-weight:400;font-size:19px;line-height:24px;color:#30343b}
.stars{margin-top:10px;font-size:13px;color:var(--star);letter-spacing:1px}
.stars span{color:#9a9ea5;margin-left:6px;font-size:12px}
.course-cat{margin-top:10px;font-family:"Montserrat",Arial,sans-serif;font-weight:600;font-size:13px;line-height:16px;color:var(--red)}
.course-dur{font-family:"Montserrat",Arial,sans-serif;font-weight:500;font-size:11px;line-height:14px;color:var(--red)}
.course-price{position:absolute;right:14px;bottom:12px;font-family:"Montserrat",Arial,sans-serif;font-weight:700;font-size:28px;color:var(--price)}
.course-rule{position:absolute;left:0;right:0;bottom:56px;border-top:1px solid #e4e6ea}
.btn{background:var(--red);color:var(--white);font-family:"Montserrat",Arial,sans-serif;font-weight:700;font-size:13px;letter-spacing:1px;display:flex;align-items:center;justify-content:center}

/* contact */
.contact{left:0;top:2588px;width:1200px;height:529px;background:radial-gradient(ellipse at 85% 30%,#1f5aa8 0,var(--navy-deep) 60%,#08306a 100%)}
.contact-title .section-title{color:var(--white);border-bottom-color:var(--white)}
.field{background:var(--white);font-family:"Montserrat",Arial,sans-serif;font-weight:600;font-size:13px;color:var(--ink);letter-spacing:1px;padding:0 18px;display:flex;align-items:center;justify-content:space-between}
.field.short{height:34px;width:413px}
.field.message{left:171px;top:2811px;width:856px;height:194px;align-items:flex-start;padding-top:14px}
.footer{left:0;top:3117px;width:1200px;height:46px;background:var(--footer);color:var(--white);font-family:"Montserrat",Arial,sans-serif;font-weight:600;font-size:13px;display:flex;align-items:center;justify-content:center}
</style>
</head>
<body>

<header class="abs hero">
  <div class="abs hero-art" role="img" aria-label="Flat illustration of hands holding a tablet playing a training video, surrounded by learning and research icons"></div>
  <div class="abs brand"><span class="brand-mark"></span>Ridgeway</div>
  <nav class="abs top-links">
    <span>
      <svg width="18" height="18" viewBox="0 0 24 24"><path fill="#fff" d="M6.6 10.8a15.1 15.1 0 0 0 6.6 6.6l2.2-2.2a1 1 0 0 1 1-.25 11.4 11.4 0 0 0 3.6.57 1 1 0 0 1 1 1V20a1 1 0 0 1-1 1A17 17 0 0 1 3 4a1 1 0 0 1 1-1h3.5a1 1 0 0 1 1 1c0 1.25.2 2.45.57 3.57a1 1 0 0 1-.25 1z"/></svg>
      555 - 014 - 278
    </span>
    <span>
      <svg width="30" height="26" viewBox="0 0 30 26" fill="none" stroke="#fff" stroke-width="2.2"><path d="M10 7V2h17v22H10v-5"/><path d="M2 13h16M13 8l5 5-5 5"/></svg>
      LOG IN
    </span>
  </nav>
</header>

<div class="abs title-band">RESEARCH AND <em>DEVELOPMENT TRAINING</em></div>

<section>
  <div class="abs about-title"><h2 class="section-title">ABOUT THE <em>PORTAL</em></h2></div>
  <p class="abs about-text">Lorem Ipsum is simply dummy text of the printing and typesetting industry. Lorem Ipsum has been the industry's standard dummy text ever since the 1500s, when an unknown printer took a galley of type and scrambled it to make a type specimen book. It has survived not only five centuries, but also the leap into electronic typesetting, remaining essentially unchanged. It was popularised in the 1960s with the release of Letraset sheets containing.Lorem Ipsum is simply dummy text of the printing and typesetting industry. Lorem Ipsum has been the industry's standard dummy text ever since the 1500s, when an unknown printer took a galley of type and scrambled it to make a type specimen book. It has survived not only five centuries, but also the leap into electronic typesetting, remaining essentially unchanged. It was popularised in the 1960s with the release of Letraset sheets containing.</p>
  <div class="abs about-art" role="img" aria-label="Desktop monitor showing a layered pyramid chart beside a smartphone with a gears illustration"></div>
</section>

<section>
  <div class="abs categories" role="img" aria-label="Light background fading into a dark silhouette of a city construction site with cranes"></div>
  <div class="abs centered" style="top:1054px"><h2 class="section-title" style="color:var(--red)">CATEGORIES</h2></div>

  <div class="row-one">
    <article class="abs cat-card" style="left:84px">
      <div class="cat-img" role="img" aria-label="Laptop displaying a process flow chart on a blue background" style="background:radial-gradient(ellipse 45% 40% at 45% 55%,#1e3550 0,rgba(30,53,80,.4) 60%,rgba(30,53,80,0) 100%),linear-gradient(160deg,#4a8ad0,#2559a3)"></div>
      <h3 class="cat-bar">METHODOLOGY</h3>
      <p class="cat-text">Lorem Ipsum is simply dummy text of the printing and typesetting industry. Lorem Ipsum has been the industry's standard dummy text ever since the 1500s.</p>
    </article>
    <article class="abs cat-card" style="left:436px">
      <div class="cat-img" role="img" aria-label="Engineers in hard hats operating equipment and reviewing plans" style="background:linear-gradient(180deg,#1fb2a6 0,#2bbfa8 46%,#7fc241 54%,#8cc63f 100%)"></div>
      <h3 class="cat-bar">EQUIPMENT</h3>
      <p class="cat-text">Lorem Ipsum is simply dummy text of the printing and typesetting industry. Lorem Ipsum has been the industry's standard dummy text ever since the 1500s.</p>
    </article>
    <article class="abs cat-card" style="left:788px">
      <div class="cat-img" role="img" aria-label="Isometric tablet with stacked reference books and documents" style="background:radial-gradient(ellipse 40% 35% at 50% 60%,rgba(70,80,110,.55),rgba(70,80,110,0) 100%),linear-gradient(160deg,#2fbccb,#1690a8)"></div>
      <h3 class="cat-bar">DESIGN REFERENCES</h3>
      <p class="cat-text">Lorem Ipsum is simply dummy text of the printing and typesetting industry. Lorem Ipsum has been the industry's standard dummy text ever since the 1500s.</p>
    </article>
  </div>

  <div class="row-two">
    <article class="abs cat-card" style="left:84px">
      <div class="cat-img" role="img" aria-label="Hand holding a green globe with a city and trees" style="background:radial-gradient(ellipse 35% 45% at 50% 45%,rgba(120,190,70,.75),rgba(120,190,70,0) 100%),linear-gradient(180deg,#3ab6e4,#8dd3ef)"></div>
      <h3 class="cat-bar active">SAFETY &amp; ENVIRONMENTAL</h3>
      <p class="cat-text">Lorem Ipsum is simply dummy text of the printing and typesetting industry. Lorem Ipsum has been the industry's standard dummy text ever since the 1500s, when an unknown printer took a galley of type and scrambled it to make a type</p>
    </article>
    <article class="abs cat-card" style="left:616px">
      <div class="cat-img" role="img" aria-label="Connected network of technology devices on a dark teal background" style="background:radial-gradient(ellipse 45% 40% at 55% 45%,rgba(60,150,190,.6),rgba(60,150,190,0) 100%),linear-gradient(160deg,#1a6e8f,#0f4a6b)"></div>
      <h3 class="cat-bar">TECHNOLOGY</h3>
      <p class="cat-text">Lorem Ipsum is simply dummy text of the printing and typesetting industry. Lorem Ipsum has been the industry's standard dummy text ever since the 1500s, when an unknown printer took a galley of type and scrambled it to make a type</p>
    </article>
  </div>
</section>

<section>
  <div class="abs centered" style="top:2023px"><h2 class="section-title">OUR <em>COURSES</em></h2></div>

  <article class="abs course" style="left:84px">
    <div class="course-img" role="img" aria-label="Presenter beside a chart board on a green background" style="background:linear-gradient(160deg,#2fae5e,#1d8a47)"></div>
    <div class="course-body">
      <h3 class="course-title">Lorem Ipsum is simply dummy text of the</h3>
      <div class="stars">★★★★★<span>( 3.1 )</span></div>
      <div class="course-cat">METHODOLOGY</div>
      <div class="course-dur">DURATION 6 WEEK</div>
    </div>
    <div class="course-rule"></div>
    <div class="course-price">$ 400</div>
  </article>
  <article class="abs course" style="left:348px">
    <div class="course-img" role="img" aria-label="Books and rising growth chart on a sky blue background" style="background:linear-gradient(160deg,#5bc3ea,#2d9fd6)"></div>
    <div class="course-body">
      <h3 class="course-title">Lorem Ipsum is simply dummy text of the</h3>
      <div class="stars">★★★★★<span>( 3.1 )</span></div>
      <div class="course-cat">METHODOLOGY</div>
      <div class="course-dur">DURATION 6 WEEK</div>
    </div>
    <div class="course-rule"></div>
    <div class="course-price">$ 400</div>
  </article>
  <article class="abs course" style="left:612px">
    <div class="course-img" role="img" aria-label="Digital globe with circuit lines on a dark blue background" style="background:radial-gradient(circle at 35% 50%,#2f6fb0,#0d2350 70%)"></div>
    <div class="course-body">
      <h3 class="course-title">Lorem Ipsum is simply dummy text of the</h3>
      <div class="stars">★★★★★<span>( 3.1 )</span></div>
      <div class="course-cat">METHODOLOGY</div>
      <div class="course-dur">DURATION 6 WEEK</div>
    </div>
    <div class="course-rule"></div>
    <div class="course-price">$ 400</div>
  </article>
  <article class="abs course" style="left:876px">
    <div class="course-img" role="img" aria-label="Rocket launching among science and idea icons on a pale green background" style="background:radial-gradient(circle at 60% 40%,#f4f1c4,#b9d77a 80%)"></div>
    <div class="course-body">
      <h3 class="course-title">Lorem Ipsum is simply dummy text of the</h3>
      <div class="stars">★★★★★<span>( 3.1 )</span></div>
      <div class="course-cat">METHODOLOGY</div>
      <div class="course-dur">DURATION 6 WEEK</div>
    </div>
    <div class="course-rule"></div>
    <div class="course-price">$ 400</div>
  </article>

  <div class="abs btn" style="left:528px;top:2503px;width:144px;height:30px">VIEW MORE</div>
</section>

<section>
  <div class="abs contact" role="img" aria-label="Deep blue background with a faint network of connected lines"></div>
  <div class="abs centered contact-title" style="top:2638px"><h2 class="section-title">CONTACT US</h2></div>
  <div class="abs field short" style="left:171px;top:2706px">NAME</div>
  <div class="abs field short" style="left:612px;top:2706px">EMAIL ID</div>
  <div class="abs field short" style="left:171px;top:2759px">PHONE NO</div>
  <div class="abs field short" style="left:612px;top:2759px">COURSE NAME
    <svg width="12" height="8" viewBox="0 0 12 8"><path d="M1 1l5 5 5-5" fill="none" stroke="#1d2a44" stroke-width="1.6"/></svg>
  </div>
  <div class="abs field message">MESSAGE</div>
  <div class="abs btn" style="left:526px;top:3022px;width:148px;height:32px">SEND MESSAGE</div>
</section>

<footer class="abs footer">© 2018. Ridgeway. All Rights Reserved.</footer>

</body>
</html>
```